Slide Master for Halvern Engines - A Systematic Hedge Fund

We are looking for someone to produce a theme and slide master for us for our investor presentations. I have uploaded a few examples of templates that we would like to have included:
Main Title
Section Title
Slides with just bullet points
Different image/table configurations with bullet points and foot notes
Biographies of different lengths
A disclaimer (no one will read this but it should still look nice and needs to be in the presentations)
I have also uploaded the company logo, business card and colour definitions. Currently we have a blue colour scheme defined, but it would be nice to get a complementary set of colours so that when we have charts with more elements we can just draw from those.
The most important thing is that the slide master must be of general use to us. We arn't looking to have a specific presentation designed for us, but a theme/style that we can apply ourselves to any presentation we need to give in the future. It should have clearly defined guidelines for where content should go (and if this is different with and without footnotes for example). We would also like it to have a similar feel to the logo/business cards, so matt colours, high contrast, but not busy.
I'm excited to see the results!

```html
<!DOCTYPE html>
<html lang="en">
<head>
<meta charset="utf-8">
<title>Halvern Engines – Slide Master</title>
<link rel="stylesheet" href="https://fonts.googleapis.com/css2?family=Montserrat:wght@600;700;800&family=Roboto:ital,wght@0,300;0,400;1,400;1,500&family=Roboto+Condensed:ital,wght@1,500&display=swap">
<style>
  :root {
    --canvas: #b3cdec;
    --navy: #0f2d5e;
    --navy-deep: #0a1a45;
    --blue: #3e7fd4;
    --white: #ffffff;
    --ink: #1a1a1a;
    --body-grey: #6b6b6b;
    --grid: #d9d9d9;
  }
  * { box-sizing: border-box; margin: 0; padding: 0; }
  html, body { width: 1200px; height: 1053px; overflow: hidden; background: var(--canvas); }
  .board { position: relative; width: 1200px; height: 1053px; }
  .slide {
    position: absolute; width: 506px; height: 284px; overflow: hidden;
    background: var(--white);
    box-shadow: 0 6px 22px rgba(40, 70, 120, 0.28);
    font-family: "Roboto", sans-serif;
  }
  .col-a { left: 82px; } .col-b { left: 612px; }
  .row-1 { top: 69px; } .row-2 { top: 384px; } .row-3 { top: 700px; }

  .photo { position: absolute; inset: 0; }
  .photo-cityscape { background: linear-gradient(180deg, #c7a56d 0%, #d9b478 22%, #9c8a72 48%, #3f5a80 72%, #163a6e 100%); }
  .photo-meeting { background: linear-gradient(160deg, #9fb8d6 0%, #dfe9f5 40%, #f4f8fc 60%, #a9c7ea 100%); }
  .photo-corridor { background: linear-gradient(100deg, #c9ced6 0%, #eef1f4 35%, #f7f8fa 60%, #d3d8df 100%); }
  .shade-bottom { position: absolute; left: 0; right: 0; bottom: 0; height: 55%;
    background: linear-gradient(180deg, rgba(15,45,94,0) 0%, rgba(15,45,94,0.75) 60%, rgba(15,45,94,0.95) 100%); }

  .brand { position: absolute; display: flex; align-items: center; gap: 4px;
    font-family: "Montserrat", sans-serif; font-weight: 700; color: var(--navy);
    text-transform: uppercase; white-space: nowrap; }
  .brand-mark { display: inline-block; background: currentColor; }
  .brand-small { top: 14px; right: 14px; font-size: 7px; letter-spacing: 0.02em; }
  .brand-small .brand-mark { width: 6px; height: 6px; }
  .brand-large { left: 25px; top: 36px; font-size: 15px; gap: 7px; }
  .brand-large .brand-mark { width: 13px; height: 13px; }
  .brand-closing { left: 44px; top: 40px; font-size: 15px; gap: 7px; color: var(--white); }
  .brand-closing .brand-mark { width: 13px; height: 13px; }

  .disclaimer { position: absolute; font-family: "Roboto Condensed", sans-serif; font-style: italic;
    font-weight: 500; font-size: 6.6px; line-height: 11px; color: var(--ink); }
  .disclaimer-light { color: var(--white); }

  .welcome-title { position: absolute; left: 274px; top: 206px; font-family: "Montserrat", sans-serif;
    font-weight: 800; font-size: 21px; color: var(--white); letter-spacing: 0.01em; }
  .welcome-body { position: absolute; left: 274px; top: 240px; width: 222px; font-size: 5.8px;
    line-height: 8.4px; color: var(--white); }

  .section-tag { position: absolute; left: 133px; top: 123px; width: 241px; height: 37px;
    background: var(--navy); color: var(--white); display: flex; align-items: center; justify-content: center;
    font-family: "Montserrat", sans-serif; font-weight: 700; font-size: 25px; letter-spacing: 0.01em; }

  .bio-title { position: absolute; left: 18px; top: 19px; font-family: "Montserrat", sans-serif;
    font-weight: 700; font-size: 21px; line-height: 30px; color: var(--ink); }
  .chart { position: absolute; left: 0; top: 0; }
  .chart text { font-family: "Roboto", sans-serif; fill: #595959; }

  .text-columns { position: absolute; left: 19px; top: 33px; width: 470px; display: flex; gap: 19px; }
  .text-column { width: 224px; font-size: 7.6px; line-height: 15px; font-weight: 300; color: var(--body-grey); }

  .slide-closing { background: var(--navy-deep); }
  .market-backdrop { position: absolute; right: 0; top: 0; width: 70%; height: 100%;
    background: radial-gradient(ellipse at 75% 45%, rgba(46,90,170,0.45) 0%, rgba(20,45,110,0.2) 45%, rgba(10,26,69,0) 75%); }
  .closing-title { position: absolute; left: 37px; top: 166px; font-family: "Montserrat", sans-serif;
    font-weight: 800; font-size: 68px; line-height: 70px; color: var(--white); letter-spacing: 0.01em; white-space: nowrap; }
  .closing-title .accent { color: var(--blue); }
</style>
</head>
<body>
<main class="board">

  <!-- Main title -->
  <section class="slide col-a row-1">
    <div class="photo photo-cityscape" role="img" aria-label="Photograph of historic college towers against a golden sunset sky"></div>
    <div class="shade-bottom"></div>
    <div class="brand brand-large"><span class="brand-mark"></span>Halvern Engines</div>
    <h1 class="welcome-title">WELCOME</h1>
    <p class="welcome-body">Lorem ipsum dolor sit amet, consectetur adipiscing elit, sed do eiusmod tempor incididunt ut labore et dolore magna aliqua ipsum suspendisse ultrices gravidus commodo viverra maecenas accumsan</p>
    <p class="disclaimer disclaimer-light" style="left:25px; top:245px;">*Disclaimer Sed ut perspiciatis unde omnis iste natus<br>error sit voluptatem accusantium</p>
  </section>

  <!-- Section title -->
  <section class="slide col-b row-1">
    <div class="photo photo-meeting" role="img" aria-label="Blurred photograph of colleagues meeting around a table with printed charts"></div>
    <div class="brand brand-small"><span class="brand-mark"></span>Halvern Engines</div>
    <h2 class="section-tag">BIOGRAPHIES</h2>
    <p class="disclaimer" style="left:19px; top:252px;">*Disclaimer Sed ut perspiciatis unde omnis iste natus<br>error sit voluptatem accusantium</p>
  </section>

  <!-- Section title, alternate -->
  <section class="slide col-a row-2">
    <div class="photo photo-corridor" role="img" aria-label="Photograph of two business people walking along a bright glass corridor"></div>
    <div class="brand brand-small"><span class="brand-mark"></span>Halvern Engines</div>
    <h2 class="section-tag">INTRODUCTION</h2>
    <p class="disclaimer" style="left:15px; top:252px;">*Disclaimer Sed ut perspiciatis unde omnis iste natus<br>error sit voluptatem accusantium</p>
  </section>

  <!-- Charts -->
  <section class="slide col-b row-2">
    <h2 class="bio-title">BIOGRAPHIES OF DIFFERENT<br>LENGTHS</h2>
    <div class="brand brand-small" style="top:26px;"><span class="brand-mark"></span>Halvern Engines</div>
    <svg class="chart" width="506" height="284" viewBox="0 0 506 284" aria-label="Two bar charts of distribution by range">
      <defs>
        <g id="grid">
          <rect x="0" y="-103.6" width="210" height="103.6" fill="none" stroke="#cfcfcf" stroke-width="0.5"/>
          <g stroke="var(--grid)" stroke-width="0.4">
            <line x1="0" x2="210" y1="-90.65" y2="-90.65"/><line x1="0" x2="210" y1="-77.7" y2="-77.7"/>
            <line x1="0" x2="210" y1="-64.75" y2="-64.75"/><line x1="0" x2="210" y1="-51.8" y2="-51.8"/>
            <line x1="0" x2="210" y1="-38.85" y2="-38.85"/><line x1="0" x2="210" y1="-25.9" y2="-25.9"/>
            <line x1="0" x2="210" y1="-12.95" y2="-12.95"/>
          </g>
          <g font-size="3.8" text-anchor="end">
            <text x="-4" y="1.3">0</text><text x="-4" y="-11.6">100</text><text x="-4" y="-24.6">200</text>
            <text x="-4" y="-37.5">300</text><text x="-4" y="-50.5">400</text><text x="-4" y="-63.4">500</text>
            <text x="-4" y="-76.4">600</text><text x="-4" y="-89.3">700</text><text x="-4" y="-102.3">800</text>
          </g>
          <g font-size="3.8" text-anchor="end">
            <text transform="translate(10 4) rotate(-30)">[151, 161]</text>
            <text transform="translate(24 4) rotate(-30)">(161, 171]</text>
            <text transform="translate(38 4) rotate(-30)">(171, 181]</text>
            <text transform="translate(52 4) rotate(-30)">(181, 191]</text>
            <text transform="translate(66 4) rotate(-30)">(191, 201]</text>
            <text transform="translate(80 4) rotate(-30)">(201, 211]</text>
            <text transform="translate(94 4) rotate(-30)">(211, 221]</text>
            <text transform="translate(108 4) rotate(-30)">(221, 231]</text>
            <text transform="translate(122 4) rotate(-30)">(231, 241]</text>
            <text transform="translate(136 4) rotate(-30)">(241, 251]</text>
            <text transform="translate(150 4) rotate(-30)">(251, 261]</text>
            <text transform="translate(164 4) rotate(-30)">(261, 271]</text>
            <text transform="translate(178 4) rotate(-30)">(271, 281]</text>
            <text transform="translate(192 4) rotate(-30)">(281, 291]</text>
            <text transform="translate(206 4) rotate(-30)">(291, 301]</text>
          </g>
        </g>
      </defs>

      <text x="141.5" y="106" font-size="7.5" text-anchor="middle">Title of Barchart</text>
      <g transform="translate(37 216.6)">
        <use href="#grid"/>
        <g transform="scale(1 -0.1295)">
          <rect x="0" width="14" height="50" fill="var(--navy)"/>
          <rect x="14" width="14" height="110" fill="var(--blue)"/>
          <rect x="28" width="14" height="75" fill="var(--navy)"/>
          <rect x="42" width="14" height="240" fill="var(--blue)"/>
          <rect x="56" width="14" height="450" fill="var(--navy)"/>
          <rect x="70" width="14" height="630" fill="var(--blue)"/>
          <rect x="84" width="14" height="720" fill="var(--navy)"/>
          <rect x="98" width="14" height="520" fill="var(--blue)"/>
          <rect x="112" width="14" height="480" fill="var(--navy)"/>
          <rect x="126" width="14" height="450" fill="var(--blue)"/>
          <rect x="140" width="14" height="205" fill="var(--navy)"/>
          <rect x="154" width="14" height="230" fill="var(--blue)"/>
          <rect x="168" width="14" height="185" fill="var(--navy)"/>
          <rect x="182" width="14" height="35" fill="var(--blue)"/>
          <rect x="196" width="14" height="110" fill="var(--navy)"/>
        </g>
      </g>

      <text x="383.5" y="106" font-size="7.5" text-anchor="middle">Title of second Barchart</text>
      <g transform="translate(279 216.6)">
        <use href="#grid"/>
        <g transform="scale(1 -0.1295)">
          <rect x="0" width="14" height="55" fill="var(--blue)"/>
          <rect x="14" width="14" height="110" fill="var(--navy)"/>
          <rect x="28" width="14" height="75" fill="var(--blue)"/>
          <rect x="42" width="14" height="240" fill="var(--navy)"/>
          <rect x="56" width="14" height="450" fill="var(--blue)"/>
          <rect x="70" width="14" height="630" fill="var(--navy)"/>
          <rect x="84" width="14" height="720" fill="var(--blue)"/>
          <rect x="98" width="14" height="520" fill="var(--navy)"/>
          <rect x="112" width="14" height="480" fill="var(--blue)"/>
          <rect x="126" width="14" height="450" fill="var(--navy)"/>
          <rect x="140" width="14" height="205" fill="var(--blue)"/>
          <rect x="154" width="14" height="230" fill="var(--navy)"/>
          <rect x="168" width="14" height="185" fill="var(--blue)"/>
          <rect x="182" width="14" height="35" fill="var(--navy)"/>
          <rect x="196" width="14" height="110" fill="var(--blue)"/>
        </g>
      </g>
    </svg>
    <p class="disclaimer" style="left:19px; top:251px;">*Disclaimer Sed ut perspiciatis unde omnis iste natus<br>error sit voluptatem accusantium</p>
  </section>

  <!-- Two-column text -->
  <section class="slide col-a row-3">
    <div class="brand brand-small"><span class="brand-mark"></span>Halvern Engines</div>
    <div class="text-columns">
      <p class="text-column">Lorem ipsum dolor sit amet, consectetur adipiscineiusmod tempor incididunt ut labore et dolore&nbsp; suspendisse ultrices gravisus commodo vivecenas accumsan lacusacilisisorem ipsum dolor sit ansectetur adipiscing eedsmod tempor &nbsp;incididunt ut labore et dolore magna suspendisse ultrices gravisus commodo vivecenas accumsaucilisisorem ipsum dolor sit amet, consectetur adipiscing eled do eiusmod tempor incididunt ut labore et dolore magna aliq ipsum isavisus commodo vivecenas accumsanorem ipsum dolor sit amet, consectetur adipiscineiusmod tempor incididunt ut labore et dolore magnasuspendisse ultrices gravisus com modo vivecenas accumsanusacilisisrem ipsum dolor sit ansectetur adipisciumsanusacilisisrem ipsum dolor sita</p>
      <p class="text-column">Lorem ipsum dolor sit amet, consectetur adipiscineiusmod tempor incididunt ut labore et dolore&nbsp; suspendisse ultrices gravisus commodo vivecenas accumsan lacusacilisisorem ipsum dolor sit ansectetur adipiscing eedsmod tempor &nbsp;incididunt ut labore et dolore magna suspendisse ultrices gravisus commodo vivecenas accumsaucilisisorem ipsum dolor sit amet, consectetur adipiscing eled do eiusmod tempor incididunt ut labore et dolore magna aliq ipsum isavisus commodo vivecenas accumsanorem ipsum dolor sit amet, consectetur adipiscineiusmod tempor incididunt ut labore et dolore magnasuspendisse ultrices gravisus com modo vivecenas accumsanusacilisisrem ipsum dolor sit ansectetur adipisciumsanusacilisisrem ipsum dolor sita</p>
    </div>
    <p class="disclaimer" style="left:19px; top:244px;">*Disclaimer Sed ut perspiciatis unde omnis iste natus<br>error sit voluptatem accusantium</p>
  </section>

  <!-- Closing -->
  <section class="slide slide-closing col-b row-3">
    <div class="market-backdrop" role="img" aria-label="Faint rising market chart glowing in deep blue"></div>
    <div class="brand brand-closing"><span class="brand-mark"></span>Halvern Engines</div>
    <h2 class="closing-title">THANK <span class="accent">YOU</span></h2>
    <p class="disclaimer disclaimer-light" style="left:39px; top:253px;">*Disclaimer Sed ut perspiciatis unde omnis iste natus<br>error sit voluptatem accusantium</p>
  </section>

</main>
</body>
</html>
```